Benefits of introducing UV light into HVAC systems

UV light is an effective way of reducing bacteria and viruses within offices and homes using a ventilation and/or air conditioning system. Clearly show the benefits in an infographic that an air conditioning company could place on their website to educate and persuade potential customers.

Target Market(s)

Commercial and domestic

```html
<!DOCTYPE html>
<html lang="en">
<head>
<meta charset="utf-8">
<title>4 Benefits of HVAC UV Lights for Your System</title>
<link rel="stylesheet" href="https://fonts.googleapis.com/css2?family=Oswald:wght@500;600;700&family=Lato:wght@400;700;900&display=swap">
<style>
  :root {
    --backdrop: #4e5253;
    --paper: #ffffff;
    --panel: #eef0f3;
    --sky: #1f8ed0;
    --sky-dark: #1671b4;
    --navy: #3b4a9d;
    --ocean: #1d88c8;
    --crimson: #a8232f;
    --lime: #b7c52b;
    --lime-text: #98a81a;
    --yellow: #f3ec2a;
    --ink: #2b2b2b;
    --tint-top: #e2e5ee;
    --tint-right: #dde9f3;
    --tint-bottom: #f4e2e3;
    --tint-left: #f1f3dd;
  }
  * { box-sizing: border-box; margin: 0; padding: 0; }
  html, body { width: 1200px; height: 1200px; overflow: hidden; }
  body { background: var(--backdrop); font-family: "Lato", sans-serif; color: var(--ink); position: relative; }

  .poster { position: absolute; left: 225px; top: 73px; width: 765px; height: 1082px; background: var(--panel); overflow: hidden; }

  .masthead { position: absolute; left: 0; top: 0; width: 765px; height: 110px;
    background: linear-gradient(90deg, #1b84c8 0%, #2a9ad8 55%, #1874b8 100%); }
  .lamp-art { position: absolute; left: 30px; top: 22px; width: 130px; height: 170px;
    background: linear-gradient(180deg, #ffffff 0%, #ffffff 48%, #2ec4f2 50%, #2ec4f2 58%, #f1f2b8 62%, rgba(241,242,184,0) 100%);
    border-radius: 14px 14px 0 0; }
  .headline { position: absolute; left: 222px; top: 12px; display: flex; align-items: center; gap: 12px; }
  .headline-number { font-family: "Oswald", sans-serif; font-weight: 700; font-size: 88px; line-height: 1; color: var(--yellow); }
  .headline-text { font-family: "Oswald", sans-serif; font-weight: 600; font-size: 40px; line-height: 1.02; color: #fff; letter-spacing: 0.3px; }
  .headline-text em { font-style: normal; color: var(--yellow); }

  .intro-band { position: absolute; left: 0; top: 110px; width: 765px; height: 82px; background: var(--paper); }
  .intro { position: absolute; left: 276px; top: 8px; width: 470px; font-size: 13.4px; line-height: 16.4px; color: #222; }

  .wheel { position: absolute; left: 0; top: 0; }

  .benefit { position: absolute; font-size: 11px; line-height: 12.9px; color: #333; }
  .benefit p { position: relative; padding-left: 20px; margin-bottom: 9px; }
  .benefit.justify p { text-align: justify; }
  .benefit p svg { position: absolute; left: 0; top: 0; width: 16px; height: 16px; }
  .benefit strong { font-weight: 900; }
  .airflow { left: 245px; top: 302px; width: 272px; }
  .airflow strong { color: var(--navy); }
  .savings { left: 541px; top: 478px; width: 136px; }
  .savings strong { color: var(--ocean); }
  .health { left: 104px; top: 466px; width: 135px; }
  .health strong { color: var(--lime-text); }
  .investment { left: 245px; top: 718px; width: 270px; }
  .investment strong { color: var(--crimson); }

  .cta-band { position: absolute; left: 0; top: 937px; width: 765px; height: 78px; background: var(--sky); }
  .cta { position: absolute; left: 0; top: 6px; width: 765px; text-align: center; color: #fff; font-size: 13.8px; line-height: 17px; }
  .cta strong { font-weight: 900; }
  .url-pill { position: absolute; left: 113px; top: 49px; width: 536px; height: 27px; border-radius: 14px;
    background: var(--navy); color: #fff; font-size: 13.6px; line-height: 27px; text-align: center; border: 1px solid #fff; }

  .footer { position: absolute; left: 0; top: 1015px; width: 765px; height: 67px; background: var(--paper); }
  .brand { position: absolute; left: 30px; top: 20px; display: flex; align-items: center; gap: 9px; }
  .brand-dot { width: 22px; height: 22px; border-radius: 50%; background: var(--crimson); }
  .brand-name { font-weight: 900; font-size: 17px; letter-spacing: 3px; color: var(--navy); text-transform: uppercase; }
  .contact { position: absolute; left: 297px; top: 15px; font-size: 13.5px; line-height: 18px; color: #222; }
  .contact div { display: flex; align-items: center; gap: 5px; }
  .contact svg { width: 11px; height: 12px; }
  .social { position: absolute; left: 638px; top: 21px; display: flex; gap: 6px; }
  .social span { width: 27px; height: 27px; border-radius: 50%; background: var(--crimson); display: block; }
</style>
</head>
<body>
<main class="poster">

  <header class="masthead">
    <div class="lamp-art" role="img" aria-label="Illustration of a UV lamp unit casting a beam of light"></div>
    <h1 class="headline">
      <span class="headline-number">4</span>
      <span class="headline-text">BENEFITS OF <em>HVAC UV LIGHTS</em><br>FOR YOUR SYSTEM</span>
    </h1>
  </header>

  <section class="intro-band">
    <p class="intro">Ultraviolet (UV) devices offer numerous benefits when added to your home’s heating and cooling system including keeping those cold &amp; flu germs at bay. If you’re concerned about how indoor air quality affects your family’s health, consider these 4 reasons to add UV lighting to your HVAC system.</p>
  </section>

  <svg class="wheel" width="765" height="937" viewBox="225 73 765 937" aria-hidden="true">
    <defs>
      <path id="arc-top" d="M388.5 390.1 A327 327 0 0 1 817.5 390.1"/>
      <path id="arc-right" d="M849.9 422.5 A327 327 0 0 1 849.9 851.5"/>
      <path id="arc-bottom" d="M388.5 883.9 A327 327 0 0 0 817.5 883.9"/>
      <path id="arc-left" d="M356.1 851.5 A327 327 0 0 1 356.1 422.5"/>
    </defs>

    <!-- pale quadrants -->
    <path d="M603 637 L385.9 419.9 A307 307 0 0 1 820.1 419.9 Z" fill="var(--tint-top)"/>
    <path d="M603 637 L820.1 419.9 A307 307 0 0 1 820.1 854.1 Z" fill="var(--tint-right)"/>
    <path d="M603 637 L820.1 854.1 A307 307 0 0 1 385.9 854.1 Z" fill="var(--tint-bottom)"/>
    <path d="M603 637 L385.9 854.1 A307 307 0 0 1 385.9 419.9 Z" fill="var(--tint-left)"/>

    <!-- outer ring segments -->
    <g fill="none" stroke-width="40">
      <use href="#arc-top" stroke="var(--navy)"/>
      <use href="#arc-right" stroke="var(--ocean)"/>
      <use href="#arc-bottom" stroke="var(--crimson)"/>
      <use href="#arc-left" stroke="var(--lime)"/>
    </g>

    <!-- ring labels -->
    <g font-family="Oswald, sans-serif" font-weight="600" font-size="21" fill="#fff" letter-spacing="1" dominant-baseline="central">
      <text><textPath href="#arc-top" startOffset="50%" text-anchor="middle">IMPROVED AIRFLOW</textPath></text>
      <text><textPath href="#arc-right" startOffset="50%" text-anchor="middle">IMPROVED ENERGY EFFICIENCY</textPath></text>
      <text><textPath href="#arc-bottom" startOffset="50%" text-anchor="middle">COST-EFECTIVE INVESTMENT</textPath></text>
      <text><textPath href="#arc-left" startOffset="50%" text-anchor="middle">IMPROVED ENERGY EFFICIENCY</textPath></text>
    </g>

    <!-- inner coloured hub -->
    <path d="M603 637 L504 538 A140 140 0 0 1 702 538 Z" fill="var(--navy)"/>
    <path d="M603 637 L702 538 A140 140 0 0 1 702 736 Z" fill="var(--ocean)"/>
    <path d="M603 637 L702 736 A140 140 0 0 1 504 736 Z" fill="var(--crimson)"/>
    <path d="M603 637 L504 736 A140 140 0 0 1 504 538 Z" fill="var(--lime)"/>

    <!-- dividers -->
    <g stroke="#fff" stroke-width="9">
      <line x1="383" y1="417" x2="823" y2="857"/>
      <line x1="823" y1="417" x2="383" y2="857"/>
    </g>
    <circle cx="603" cy="637" r="63" fill="#fff"/>
    <text x="603" y="641" text-anchor="middle" font-family="Lato, sans-serif" font-weight="900" font-size="13" fill="var(--navy)">Northvale Air</text>

    <!-- hub icons -->
    <g fill="none" stroke="#fff" stroke-width="3" stroke-linecap="round">
      <!-- fan -->
      <circle cx="608" cy="533" r="12"/>
      <circle cx="608" cy="533" r="3" fill="#fff"/>
      <path d="M598 508 q3 -4 0 -8 M604 508 q3 -4 0 -8 M610 508 q3 -4 0 -8 M616 508 q3 -4 0 -8"/>
      <path d="M598 558 q3 4 0 8 M604 558 q3 4 0 8 M610 558 q3 4 0 8 M616 558 q3 4 0 8"/>
      <!-- plug -->
      <rect x="688" y="620" width="22" height="26" rx="4"/>
      <line x1="693" y1="610" x2="693" y2="620"/>
      <line x1="705" y1="610" x2="705" y2="620"/>
      <path d="M699 646 v10 q0 12 14 12 q14 0 14 -12 v-40"/>
      <!-- heart -->
      <path d="M505 662 c-12 -10 -22 -17 -22 -27 a10 10 0 0 1 22 -3 a10 10 0 0 1 22 3 c0 10 -10 17 -22 27 z"/>
      <line x1="505" y1="631" x2="505" y2="647"/>
      <line x1="497" y1="639" x2="513" y2="639"/>
      <!-- dollar -->
      <circle cx="614" cy="734" r="13" fill="#fff" stroke="none"/>
      <path d="M590 758 q14 10 28 6 l20 -10" />
    </g>
    <text x="614" y="740" text-anchor="middle" font-family="Lato, sans-serif" font-weight="900" font-size="16" fill="var(--crimson)">$</text>
  </svg>

  <div class="benefit airflow justify">
    <p><svg viewBox="0 0 16 16"><rect x="1" y="3" width="12" height="12" fill="none" stroke="#3b4a9d" stroke-width="1.5"/><path d="M3 9 l3 3 l8 -11" fill="none" stroke="#3b4a9d" stroke-width="2"/></svg>UV lighting works to <strong>prevent microbial buildup</strong> on air filters, cooling coils, drain pans &amp; duct surfaces. By eliminating contaminant build-up inside your HVAC system, heat exchange and airflow are both dramatically improved.</p>
    <p><svg viewBox="0 0 16 16"><rect x="1" y="3" width="12" height="12" fill="none" stroke="#3b4a9d" stroke-width="1.5"/><path d="M3 9 l3 3 l8 -11" fill="none" stroke="#3b4a9d" stroke-width="2"/></svg>The major benefits include reducing your home’s energy use, <strong>improving indoor air quality</strong> &amp; reducing overall maintenance costs for your HVAC system.</p>
  </div>

  <div class="benefit savings">
    <p><svg viewBox="0 0 16 16"><rect x="1" y="3" width="12" height="12" fill="none" stroke="#1d88c8" stroke-width="1.5"/><path d="M3 9 l3 3 l8 -11" fill="none" stroke="#1d88c8" stroke-width="2"/></svg>Adding a UV device to your existing HVAC system can <strong>reduce your home’s overall energy consumption</strong> by up to 35%</p>
    <p><svg viewBox="0 0 16 16"><rect x="1" y="3" width="12" height="12" fill="none" stroke="#1d88c8" stroke-width="1.5"/><path d="M3 9 l3 3 l8 -11" fill="none" stroke="#1d88c8" stroke-width="2"/></svg>UV <strong>restores the HVAC system’s performance to optimal levels</strong>, reducing its power consumption and helping it work like new.</p>
  </div>

  <div class="benefit health">
    <p><svg viewBox="0 0 16 16"><rect x="1" y="3" width="12" height="12" fill="none" stroke="#98a81a" stroke-width="1.5"/><path d="M3 9 l3 3 l8 -11" fill="none" stroke="#98a81a" stroke-width="2"/></svg>Your HVAC system circulates the air in your home, which means that it also circulates airborne bacteria and viruses</p>
    <p><svg viewBox="0 0 16 16"><rect x="1" y="3" width="12" height="12" fill="none" stroke="#98a81a" stroke-width="1.5"/><path d="M3 9 l3 3 l8 -11" fill="none" stroke="#98a81a" stroke-width="2"/></svg>The UV lighting used in HVAC systems <strong>prevents the buildup of organic material</strong> on the system’s interior mechanics, killing pathogens &amp; other microorganisms that would normally thrive in an HVAC system.</p>
  </div>

  <div class="benefit investment justify">
    <p><svg viewBox="0 0 16 16"><rect x="1" y="3" width="12" height="12" fill="none" stroke="#a8232f" stroke-width="1.5"/><path d="M3 9 l3 3 l8 -11" fill="none" stroke="#a8232f" stroke-width="2"/></svg>When you add a UV lighting device to the HVAC system, you’re <strong>helping the system keep itself clean</strong>, which is why UV installations are so cost-effective when you consider all of the health-related and money-saving benefits.</p>
    <p><svg viewBox="0 0 16 16"><rect x="1" y="3" width="12" height="12" fill="none" stroke="#a8232f" stroke-width="1.5"/><path d="M3 9 l3 3 l8 -11" fill="none" stroke="#a8232f" stroke-width="2"/></svg>UV lighting in your HVAC system can also <strong>boost your home’s value</strong> and make it more attractive to potential buyers.</p>
  </div>

  <section class="cta-band">
    <p class="cta">Whether you’re just beginning to consider UV technology or you’ve already decided to go ahead<br>with the installation, &nbsp;call <strong>Northvale Air at (555) 014-2283</strong> to get started</p>
    <div class="url-pill">www.northvaleair.com/blog/4-benefits-of-hvac-uv-lights-for-your-system/</div>
  </section>

  <footer class="footer">
    <div class="brand"><span class="brand-dot"></span><span class="brand-name">Northvale Air</span></div>
    <div class="contact">
      <div><svg viewBox="0 0 12 12"><path d="M2 1 l3 0 l1 3 l-2 1 q1 2 3 3 l1 -2 l3 1 l0 3 q-8 0 -9 -9 z" fill="#a8232f"/></svg>(555) 014-2283</div>
      <div><svg viewBox="0 0 12 12"><path d="M6 12 q-5 -6 -5 -7 a5 5 0 0 1 10 0 q0 1 -5 7 z" fill="#a8232f"/><circle cx="6" cy="5" r="2" fill="#fff"/></svg>418 Cedar Ridge Road Millbrook, AZ 86000</div>
    </div>
    <div class="social" aria-label="Social links"><span></span><span></span><span></span></div>
  </footer>

</main>
</body>
</html>
```